American cannabis tech company business card design

Quillo.com is seeking a modern, professional, and brand-aligned business card that represents our company and its core values: Mission, Story, Values, and Impact. As an innovative cannabis company, we want a business card that is not only visually appealing but also serves as a representation of who we are and what we stand for.

Project Scope: Design a double-sided business card that integrates our brand identity and core values. Incorporate our key brand elements, ensuring a sleek and contemporary aesthetic. Visually reflect our core values (Mission, Story, Values, Impact) in a way that is engaging yet professional.

Target Market(s)

Vendors, third parties,

Contact Information for Business Card

Contact details (name, title, email, phone, website, etc.)

Font styles to use
Other font styles liked:
• Caslon, Centra

Colors

Designer to choose colors to be used in the design.

Requirements
Must have
• Quillo.com logo and branding A creative yet clean way to integrate our core values (Mission, Story, Values, Impact) Modern typography and a well-structured layout
Nice to have
• forest green, grey, white, black
Should not have
• references to marijuana, leafs, plants, or related product

```html
<!DOCTYPE html>
<html lang="en">
<head>
<meta charset="UTF-8">
<title>Quillo Business Card</title>
<link href="https://fonts.googleapis.com/css2?family=Poppins:wght@400;500;600;800&display=swap" rel="stylesheet">
<style>
  :root {
    --backdrop: #232221;
    --forest: #1a321b;
    --paper: #efefef;
    --ink-light: #ffffff;
    --shadow: rgba(0, 0, 0, 0.55);
  }
  * { margin: 0; padding: 0; box-sizing: border-box; }
  html, body {
    width: 1064px; height: 1200px; overflow: hidden;
    background: var(--backdrop);
    font-family: "Poppins", sans-serif;
  }
  .canvas { position: relative; width: 1064px; height: 1200px; }
  .card {
    position: absolute;
    width: 629px; height: 390px;
    box-shadow: 3px 4px 6px var(--shadow);
  }
  .card-front {
    left: 266px; top: 140px;
    background: var(--forest);
    border-radius: 0 195px 195px 0;
    color: var(--ink-light);
  }
  .card-back {
    left: 233px; top: 584px;
    background: var(--paper);
    border-radius: 195px 0 0 195px;
  }
  .brand-name {
    font-weight: 800;
    letter-spacing: -1px;
    line-height: 1;
    white-space: nowrap;
  }
  .card-front .brand-name {
    position: absolute; left: 34px; top: 197px;
    transform: translateY(-50%);
    font-size: 65px; color: var(--ink-light);
  }
  .card-back .brand-name {
    position: absolute; left: 50%; top: 194px;
    transform: translate(-50%, -50%);
    font-size: 82px; color: var(--forest);
  }
  .core-values {
    position: absolute; left: 50%; top: 252px;
    transform: translateX(-50%);
    display: flex; align-items: center; gap: 10px;
    list-style: none; white-space: nowrap;
    font-size: 13px; font-weight: 500; letter-spacing: 2.5px;
    color: var(--forest);
  }
  .core-values li + li::before {
    content: ""; display: inline-block;
    width: 4px; height: 4px; border-radius: 50%;
    background: var(--forest);
    margin-right: 10px; vertical-align: middle;
    transform: translateY(-1px);
  }
  .divider {
    position: absolute; left: 291px; top: 122px;
    width: 1px; height: 170px; background: var(--ink-light);
  }
  .details { position: absolute; left: 317px; top: 104px; }
  .person-name { font-size: 26px; font-weight: 600; line-height: 1.2; }
  .person-title { font-size: 19px; font-weight: 400; line-height: 1.2; }
  .contact-list { list-style: none; margin-top: 17px; }
  .contact-list li {
    display: flex; align-items: center; gap: 6px;
    font-size: 18.5px; line-height: 23px;
  }
  .contact-list svg { width: 16px; height: 16px; flex: none; }
  .address { margin-top: 16px; font-size: 18.5px; line-height: 24px; padding-left: 2px; }
</style>
</head>
<body>
<div class="canvas">
  <section class="card card-front">
    <div class="brand-name">QUILLO</div>
    <div class="divider"></div>
    <div class="details">
      <div class="person-name">DANIEL HARPER</div>
      <div class="person-title">Managing Director</div>
      <ul class="contact-list">
        <li>
          <svg viewBox="0 0 16 16" fill="none" stroke="#fff" stroke-width="1.6" stroke-linejoin="round"><path d="M3 1.5l3 .5 1 3-2 1.5a9 9 0 004.5 4.5L11 9l3 1 .5 3-2 1.5C7 14 2 9 1.5 3.5z"/></svg>
          044-987 654 321
        </li>
        <li>
          <svg viewBox="0 0 16 16"><rect x="1" y="3" width="14" height="10" fill="#fff"/><path d="M1.5 3.5L8 9l6.5-5.5" fill="none" stroke="#1a321b" stroke-width="1.4"/></svg>
          hello@quillo.com
        </li>
        <li>
          <svg viewBox="0 0 16 16" fill="none" stroke="#fff" stroke-width="1.3"><circle cx="8" cy="8" r="6.5"/><ellipse cx="8" cy="8" rx="3" ry="6.5"/><path d="M1.5 8h13M2.5 4.8h11M2.5 11.2h11"/></svg>
          www.quillo.com
        </li>
      </ul>
      <p class="address">421, Address line name<br>goes here 45452,Country</p>
    </div>
  </section>
  <section class="card card-back">
    <div class="brand-name">QUILLO</div>
    <ul class="core-values">
      <li>MISSION</li>
      <li>STORY</li>
      <li>VALUES</li>
      <li>IMPACT</li>
    </ul>
  </section>
</div>
</body>
</html>
```